Food Safety 1-California workers only

3.25" by 4.5" Black and White Magazine Ad
This ad is to train California workers only.
Workers will be trained on: Food Safety, FSMA (Food Safety Modernization Act), using equipment safety, food processing production skills, worker safety, supervisory skills, communication skills.
"FREE TRAINING", The company does the training or Keystone Learning will provide the training.
Training grants range from $100,000 to $400,000.
Companies must be in business for profit.
Companies must train 200 employees or more.
This program is for California workers only.
Incumbent or new-hires are eligible.

Target Market(s)

California food processors, farms, food packaging, food processors, companies under FSMA, food safety, food production who need to train employees.

Industry/Entity Type

Food Production

Font styles to use
Serif
Sans Serif

Colors

Designer to choose colors to be used in the design.

Requirements
Must have
• This is a 3.25 inch by 4.5 inch magazine ad. It must be black and white. No color.
• The deliverable must be in basic PhotoShop. The ad does not need to include any graphics and be text only if needed. If you have a black and white graphic that will show well.
• Look at www.KLGFoodSafety..com
• Use the text from "MEALBOX-Photoshop-052018" file as your starting point.
Nice to have
• A black and white graphic about food. See www.KLGFoodSafety.com
Should not have
• No color.

```html
<!DOCTYPE html>
<html lang="en">
<head>
<meta charset="utf-8">
<title>Free Training – KLG Food Safety</title>
<link rel="stylesheet" href="https://fonts.googleapis.com/css2?family=Bebas+Neue&family=Bodoni+Moda:ital@1&family=Open+Sans:wght@400;700&display=swap">
<style>
  :root {
    --backdrop: #ececec;
    --paper: #ffffff;
    --ink: #111111;
    --band: #000000;
    --band-text: #ffffff;
    --muted: #555555;
  }
  * { box-sizing: border-box; margin: 0; padding: 0; }
  html, body { width: 1200px; height: 1000px; overflow: hidden; }
  body {
    background: var(--backdrop);
    font-family: "Open Sans", Arial, sans-serif;
    color: var(--ink);
    position: relative;
  }
  .ad {
    position: absolute;
    left: 249px; top: 20px;
    width: 698px; height: 967px;
    background: var(--paper);
    box-shadow: 0 2px 8px rgba(0,0,0,0.25);
  }
  .brand {
    position: absolute;
    top: 46px; left: 0; width: 100%;
    display: flex; justify-content: center; align-items: center; gap: 8px;
    font-family: "Open Sans", Arial, sans-serif;
    font-weight: 700; font-size: 15px; letter-spacing: 0.5px;
    color: var(--ink);
  }
  .brand-mark { width: 14px; height: 14px; background: var(--ink); }
  .headline {
    position: absolute;
    top: 92px; left: 0; width: 100%;
    text-align: center;
    font-family: "Bebas Neue", Impact, sans-serif;
    font-size: 122px; line-height: 1;
    letter-spacing: 2px;
  }
  .topics {
    position: absolute;
    top: 202px; left: 0; width: 100%;
    text-align: center;
    font-family: "Bebas Neue", Impact, sans-serif;
    font-size: 27px; letter-spacing: 0.3px;
  }
  .tagline {
    position: absolute;
    top: 250px; left: 0; width: 100%;
    text-align: center;
    font-family: "Bodoni Moda", Georgia, serif;
    font-style: italic; font-size: 31px;
  }
  .qualify {
    position: absolute;
    top: 307px; left: 0; width: 100%; height: 419px;
    background: var(--band);
    color: var(--band-text);
  }
  .qualify-title {
    text-align: center;
    font-family: "Bebas Neue", Impact, sans-serif;
    font-size: 50px; line-height: 1;
    margin-top: 20px; letter-spacing: 0.5px;
  }
  .criteria { list-style: none; margin-top: 8px; }
  .criterion {
    display: flex; justify-content: center; align-items: flex-start; gap: 12px;
    font-size: 19px; line-height: 26px;
    text-align: center;
    margin-bottom: 21px;
  }
  .criterion.two-line { margin-bottom: 15px; }
  .tick { width: 22px; height: 22px; flex: none; margin-top: 3px; }
  .contact {
    position: absolute;
    left: 39px; top: 748px;
    width: 620px; height: 192px;
    border: 1.5px dashed var(--ink);
    border-radius: 32px;
    text-align: center;
    padding-top: 11px;
    font-size: 19.5px; line-height: 29px;
  }
  .contact-name { font-weight: 700; font-size: 18px; letter-spacing: 0.5px; }
  .contact-line { display: flex; justify-content: center; align-items: center; gap: 10px; font-size: 18px; line-height: 30px; }
  .contact-icon { width: 22px; height: 22px; }
  .sep { margin: 0 4px; }
</style>
</head>
<body>
<svg width="0" height="0" style="position:absolute">
  <defs>
    <symbol id="tick-icon" viewBox="0 0 24 24">
      <circle cx="12" cy="12" r="10" fill="none" stroke="currentColor" stroke-width="1.8"/>
      <path d="M7 12.5l3.2 3.2L18 7" fill="none" stroke="currentColor" stroke-width="2.2" stroke-linecap="round" stroke-linejoin="round"/>
    </symbol>
  </defs>
</svg>

<main class="ad">
  <div class="brand"><span class="brand-mark"></span>KLG FOOD SAFETY</div>
  <h1 class="headline">FREE TRAINING</h1>
  <p class="topics">FOOD SAFETY &nbsp;•&nbsp; FSMA &nbsp;•&nbsp; PRODUCTION SKILLS &nbsp;•&nbsp; WORKER SAFETY</p>
  <p class="tagline">We do the training and the state pays for it!</p>

  <section class="qualify">
    <h2 class="qualify-title">HOW TO QUALIFY</h2>
    <ul class="criteria">
      <li class="criterion"><svg class="tick"><use href="#tick-icon"/></svg><span>Train California Workers Only</span><svg class="tick"><use href="#tick-icon"/></svg></li>
      <li class="criterion"><svg class="tick"><use href="#tick-icon"/></svg><span>Trainees must earn $11/hour</span><svg class="tick"><use href="#tick-icon"/></svg></li>
      <li class="criterion"><svg class="tick"><use href="#tick-icon"/></svg><span>Full-time workers only</span><svg class="tick"><use href="#tick-icon"/></svg></li>
      <li class="criterion two-line"><svg class="tick"><use href="#tick-icon"/></svg><span>Employees must attend at<br>least 8 Hours of training</span><svg class="tick"><use href="#tick-icon"/></svg></li>
      <li class="criterion"><svg class="tick"><use href="#tick-icon"/></svg><span>You must train 200 or more employees</span><svg class="tick"><use href="#tick-icon"/></svg></li>
      <li class="criterion"><svg class="tick"><use href="#tick-icon"/></svg><span>Incumbent or New-Hire workers are eligible</span><svg class="tick"><use href="#tick-icon"/></svg></li>
      <li class="criterion"><svg class="tick"><use href="#tick-icon"/></svg><span>Seasonal workers are eligible</span><svg class="tick"><use href="#tick-icon"/></svg></li>
    </ul>
  </section>

  <address class="contact" style="font-style:normal">
    <div class="contact-name">DANIEL HARPER</div>
    <div>Keystone Learning Company, Inc.</div>
    <div>2700 Meadowbrook Avenue Suite 310 Irvine, CA 92614</div>
    <div class="contact-line">
      <svg class="contact-icon" viewBox="0 0 24 24" fill="none" stroke="currentColor" stroke-width="1.5"><circle cx="12" cy="12" r="10"/><ellipse cx="12" cy="12" rx="4.5" ry="10"/><path d="M2 12h20M4 7h16M4 17h16"/></svg>
      <span>www.KLGCAL.com <span class="sep">|</span> www.KLGFoodSafety.com</span>
    </div>
    <div class="contact-line">
      <svg class="contact-icon" viewBox="0 0 24 24" fill="none" stroke="currentColor" stroke-width="1.5"><circle cx="12" cy="12" r="10.5"/><rect x="6.5" y="8" width="11" height="8" rx="1"/><path d="M6.5 8.5l5.5 4.5 5.5-4.5"/></svg>
      <span>dan.harper@klgcal.com</span>
    </div>
    <div class="contact-line">
      <svg class="contact-icon" viewBox="0 0 24 24" fill="none" stroke="currentColor" stroke-width="1.5"><circle cx="12" cy="12" r="10.5"/><path d="M8.5 6.5l2 2.5-1.3 1.6c.8 1.7 2.3 3.2 4 4l1.6-1.3 2.5 2-1.2 1.8c-4.3-.3-8.6-4.6-8.9-8.9z" fill="currentColor"/></svg>
      <span>(949) 555-0142</span>
    </div>
  </address>
</main>
</body>
</html>
```